New Infographic Design Project

Hi, I have another project to work on if you are interested. It is a horizontal style infographic with 6 steps. It should display the step Number (1-6), Title, and an Icon.

Step 1 - Strong Phone Interview
Step 2 - Pre-Employment
Step 3 - Prep & Do In-Person Interview
Step 4 - Second Interview
Step 5 - Reference Checks
Step 6 - Job Offer

More flexible on colors with this one, but keep it professional.

```html
<!DOCTYPE html>
<html lang="en">
<head>
<meta charset="utf-8">
<title>Hiring Process – Six Steps</title>
<link rel="stylesheet" href="https://fonts.googleapis.com/css2?family=Bebas+Neue&family=Open+Sans:wght@400&display=swap">
<style>
  :root {
    --bg-dark: #7f8890;
    --bg-mid: #b4bcc3;
    --bg-light: #e6eaee;
    --panel-light: #f7f8f9;
    --panel-dark: #bcc2c8;
    --card: #f3f4f5;
    --card-edge: #ffffff;
    --card-line: #d9dbdd;
    --ink: #3a3a3c;
    --step-1: #2e3a86;
    --step-2: #e7a7e1;
    --step-3: #4a4536;
    --step-4: #5f9a8f;
    --step-5: #a99a83;
    --step-6: #c27a45;
  }
  html, body {
    margin: 0;
    padding: 0;
    width: 1200px;
    height: 1000px;
    overflow: hidden;
  }
  .canvas {
    position: relative;
    width: 1200px;
    height: 1000px;
    overflow: hidden;
    background:
      radial-gradient(ellipse at 80% 10%, rgba(255,255,255,.55), transparent 45%),
      radial-gradient(ellipse at 15% 95%, rgba(255,255,255,.5), transparent 40%),
      linear-gradient(160deg, var(--bg-light) 0%, var(--bg-dark) 35%, var(--bg-mid) 60%, var(--bg-light) 100%);
  }
  .backdrop-swoosh {
    position: absolute;
    inset: 0;
  }
  .panel {
    position: absolute;
    left: 12px;
    top: 255px;
    width: 1176px;
    height: 490px;
    background: linear-gradient(100deg, var(--panel-light) 0%, #eceef0 45%, var(--panel-dark) 100%);
    box-shadow: 0 2px 6px rgba(0,0,0,.15);
  }
  .step-card {
    position: absolute;
    top: 352px;
    width: 142px;
    height: 255px;
    border-radius: 22px;
    background: var(--card-edge);
    box-shadow: 10px 14px 18px rgba(0,0,0,.22);
  }
  .step-card__inner {
    position: absolute;
    inset: 5px;
    border-radius: 18px;
    border: 1px solid var(--card-line);
    background: linear-gradient(180deg, #fbfbfb 0%, var(--card) 100%);
  }
  .step-card__badge {
    position: absolute;
    left: 50%;
    top: 15px;
    width: 94px;
    height: 94px;
    margin-left: -47px;
    border-radius: 50%;
    background: var(--accent);
    box-shadow: 3px 5px 8px rgba(0,0,0,.25);
  }
  .step-card__icon {
    position: absolute;
    inset: 7px;
    border-radius: 50%;
    background: radial-gradient(circle at 40% 35%, #ffffff 0%, #eceded 70%, #dcdddf 100%);
  }
  .step-card__label {
    position: absolute;
    top: 120px;
    left: 0;
    right: 0;
    text-align: center;
    font-family: "Bebas Neue", "Arial Narrow", sans-serif;
    font-size: 18px;
    letter-spacing: .5px;
    color: var(--ink);
  }
  .step-card__rule {
    position: absolute;
    top: 145px;
    left: 50%;
    width: 92px;
    margin-left: -46px;
    border-top: 2px dashed var(--accent);
  }
  .step-card__title {
    position: absolute;
    top: 160px;
    left: 6px;
    right: 6px;
    text-align: center;
    font-family: "Bebas Neue", "Arial Narrow", sans-serif;
    font-size: 23px;
    line-height: 22px;
    color: var(--ink);
  }
  .step-card__title small {
    display: block;
    font-size: 16px;
    line-height: 18px;
  }
  .format-note {
    position: absolute;
    top: 916px;
    left: 0;
    width: 1200px;
    text-align: center;
    font-family: "Open Sans", Arial, sans-serif;
    font-size: 17px;
    color: #111;
    letter-spacing: .2px;
  }
</style>
</head>
<body>
<div class="canvas">
  <svg class="backdrop-swoosh" width="1200" height="1000" viewBox="0 0 1200 1000" aria-hidden="true">
    <path d="M620 0 C760 120 960 180 1200 170 L1200 230 C950 240 760 160 600 0 Z" fill="rgba(255,255,255,.35)"/>
    <path d="M0 860 C220 780 460 800 700 1000 L600 1000 C420 860 220 840 0 900 Z" fill="rgba(255,255,255,.35)"/>
  </svg>

  <div class="panel"></div>

  <div class="step-card" style="left:92px; --accent: var(--step-1);">
    <div class="step-card__inner">
      <div class="step-card__badge"><div class="step-card__icon" role="img" aria-label="Icon: person on a phone call"></div></div>
      <div class="step-card__label">Step 1</div>
      <div class="step-card__rule"></div>
      <div class="step-card__title">Strongphone<br>interview</div>
    </div>
  </div>

  <div class="step-card" style="left:264px; --accent: var(--step-2);">
    <div class="step-card__inner">
      <div class="step-card__badge"><div class="step-card__icon" role="img" aria-label="Icon: computer screen with a form"></div></div>
      <div class="step-card__label">Step 2</div>
      <div class="step-card__rule"></div>
      <div class="step-card__title">Pre-<br>employment</div>
    </div>
  </div>

  <div class="step-card" style="left:436px; --accent: var(--step-3);">
    <div class="step-card__inner">
      <div class="step-card__badge"><div class="step-card__icon" role="img" aria-label="Icon: two people talking at a desk"></div></div>
      <div class="step-card__label">Step 3</div>
      <div class="step-card__rule"></div>
      <div class="step-card__title">Prep&amp;amp;<br>amp;doin-<small>personinterview</small></div>
    </div>
  </div>

  <div class="step-card" style="left:606px; --accent: var(--step-4);">
    <div class="step-card__inner">
      <div class="step-card__badge"><div class="step-card__icon" role="img" aria-label="Icon: two people in conversation"></div></div>
      <div class="step-card__label">Step 4</div>
      <div class="step-card__rule"></div>
      <div class="step-card__title">Second<br>interview</div>
    </div>
  </div>

  <div class="step-card" style="left:776px; --accent: var(--step-5);">
    <div class="step-card__inner">
      <div class="step-card__badge"><div class="step-card__icon" role="img" aria-label="Icon: person with an approved document"></div></div>
      <div class="step-card__label">Step 5</div>
      <div class="step-card__rule"></div>
      <div class="step-card__title">Reference<br>checks</div>
    </div>
  </div>

  <div class="step-card" style="left:946px; --accent: var(--step-6);">
    <div class="step-card__inner">
      <div class="step-card__badge"><div class="step-card__icon" role="img" aria-label="Icon: contract with a shield and tick"></div></div>
      <div class="step-card__label">Step 6</div>
      <div class="step-card__rule"></div>
      <div class="step-card__title">Joboffer</div>
    </div>
  </div>

  <p class="format-note">VECTORIAL MATERIAL IN FORMAT -PDF-AI-EPS-AVS- PNG-JPG.</p>
</div>
</body>
</html>
```